Vina Solvara

Solvara embodies the purity and intensity of Chile’s cold coastal terroir. The sleek white label and bold X logo reflect the stark beauty and unrelenting nature of these extreme winemaking conditions. Crisp, vibrant, and refreshingly bold, Solvara is a tribute to the wild energy of the Pacific winds and the cool embrace of the coastal valleys—a wine for those who seek purity and perfection in every sip. We would like to have a simple design focusing o the X, we try some option see attach but we are no satisfied is not enaguh eyes catching
Updates

Please create a mysterious, enigmatic label based on the typography and logo attached to the project. We need at least, at the entry level, five varietal products such as Carménère, Cabernet Sauvignon, Merlot, Chardonnay, and Malbec. Later, we would like to add more premium products, like a Reserva, a Special Reserva, or a Limited Edition. The design should be flexible and easily adaptable to accommodate various products while maintaining the same overall aesthetic.

I upload some wines label with printing technic we would like to use on our label, please incorporate this into your design

Project Brief – Large-Scale Brand Label Design
We are developing a new large-scale brand with a structured range of wines. Below are the key design elements and specifications for the labels:

Pinot Noir, Chardonnay, Syrah (Burgundy bottle shape – must include "Special Reserve" on the label)
General Label Guidelines
Year: Only mention "2024" (do not include the word “vintage”).
Capsules: Use standard-colored capsules only (no branding).
Label Design:
Focus on the label itself; bottle and background are irrelevant.
We can consider a wraparound label, but space must be reserved for back-label information.
Please refer to www.pelnorth-wines.example for brand coherence. Let us know if further details are needed.

Target Market(s)

peopels who looking for simple design but strinking with the X . THe X could be like a painting brush somehting which make it look artistic

Industry/Entity Type

Wines producer

Font styles to use
Decorative
Script
Other font styles liked:
• the X would be nice if it look like he is Brush from a painter

Colors
0054AA
0677BA
7BADD7
CADEEF
E8F1F8
FFF300
FFF600
FEFA6F
FFFEC7
FFFEE8
EB3D1F
EC4F4E
F09395
F8D3D4
FCEDEE

Requirements
Must have
• We need to indicate the varietals Cabernet Sauvignon, the vintage 2024, the region DO Central Valley
Nice to have
• option on a burgendy bottle for chardonnay and pinot noir and option on bordeau bottle for Cabernet sauvignon and Merlot, We will need a large serie of 5 entrance lebvel (4 red one white) 2 reserve, 2 special reserve, 2 Limited

```html
<!DOCTYPE html>
<html lang="en">
<head>
<meta charset="utf-8">
<title>Solvara – Cabernet Sauvignon Label</title>
<link rel="stylesheet" href="https://fonts.googleapis.com/css2?family=Archivo:wght@400;800&display=swap">
<style>
  :root {
    --paper: #ffffff;
    --ink: #1b2336;
    --wave-teal: #2b8f99;
    --wave-light: #cfe6e6;
    --wave-deep: #1e3a4c;
    --wave-orange: #e0892d;
    --wave-rust: #b4482a;
  }
  html, body {
    margin: 0;
    width: 1200px;
    height: 1200px;
    overflow: hidden;
    background: var(--paper);
  }
  .label {
    position: absolute;
    left: 163px;
    top: 100px;
    width: 874px;
    height: 1000px;
    overflow: hidden;
    font-family: "Archivo", sans-serif;
    color: var(--ink);
  }
  .label__artwork {
    position: absolute;
    inset: 0;
    background:
      radial-gradient(ellipse 38% 26% at 50% 18%, rgba(232,240,240,0.95) 0%, rgba(232,240,240,0) 100%),
      radial-gradient(ellipse 30% 40% at 8% 70%, rgba(224,137,45,0.55) 0%, rgba(224,137,45,0) 100%),
      radial-gradient(ellipse 25% 35% at 95% 65%, rgba(180,72,42,0.5) 0%, rgba(180,72,42,0) 100%),
      linear-gradient(160deg, var(--wave-light) 0%, var(--wave-teal) 35%, var(--wave-deep) 60%, var(--wave-teal) 85%, var(--wave-light) 100%);
  }
  .label__panel {
    position: absolute;
    inset: 0;
  }
  .brand-mark {
    position: absolute;
    top: 190px;
    left: 0;
    width: 100%;
    text-align: center;
    font-weight: 800;
    font-size: 96px;
    letter-spacing: 6px;
    color: var(--ink);
    line-height: 1;
  }
  .brand-mark__dot {
    display: inline-block;
    width: 22px;
    height: 22px;
    border-radius: 50%;
    background: var(--ink);
    margin-left: 14px;
    vertical-align: middle;
  }
  .wordmark {
    position: absolute;
    top: 500px;
    left: 200px;
    width: 500px;
    text-align: center;
    font-weight: 800;
    font-size: 76px;
    letter-spacing: 6px;
    line-height: 1;
    transform: rotate(1deg);
  }
  .varietal {
    position: absolute;
    top: 660px;
    left: 200px;
    width: 500px;
    text-align: center;
    font-weight: 400;
    font-size: 30px;
    letter-spacing: 3px;
  }
  .vintage {
    position: absolute;
    top: 702px;
    left: 200px;
    width: 500px;
    text-align: center;
    font-size: 24px;
    letter-spacing: 1px;
  }
  .appellation {
    position: absolute;
    top: 790px;
    left: 200px;
    width: 500px;
    text-align: center;
    font-size: 24px;
    letter-spacing: 0.5px;
  }
  .label__accent-dot {
    position: absolute;
    left: 190px;
    top: 778px;
    width: 44px;
    height: 44px;
    border-radius: 50%;
    background: var(--ink);
  }
</style>
</head>
<body>
  <section class="label">
    <div class="label__artwork" role="img" aria-label="Painted illustration of swirling Pacific waves in teal, navy, white and orange streaks filling the label"></div>
    <svg class="label__panel" width="874" height="1000" viewBox="0 0 874 1000" aria-hidden="true">
      <path fill="#ffffff" d="M215,600 C220,520 320,470 370,420 L520,420 C560,470 690,520 700,600 L705,800 C700,860 640,870 560,870 C450,880 350,930 245,890 C205,870 200,830 205,780 Z"/>
    </svg>
    <div class="brand-mark">SOLVARA<span class="brand-mark__dot"></span></div>
    <h1 class="wordmark">SOLVARA</h1>
    <p class="varietal">CABERNET SAUVIGNON</p>
    <p class="vintage">VINTAGE 2024</p>
    <div class="label__accent-dot"></div>
    <p class="appellation">DO CENTRAL VALLEY</p>
  </section>
</body>
</html>
```